Brivel Mobile generic phone package design

Hello, We are a new wireless carrier and we need a simple but impressive looking design for our generic Brivel Mobile phone box. I have included a box design idea we've been playing with, just to show the simplicity of it. Dimension of the box should 4.5x7.5x2 inches. We do have a website if you'd like to look at our company, attached a few pictures, our Logo and a the wallpaper we like to use. Our slogan is " Now I Can REALLY Hear You!" that we'd like to have on the box, the logo as well and our website address "brivelmobile.example". Just a few things to mention that are important in the design. Of course if you have great vision and would like to provide us with a great design completely different from what we've envisioned would love to see it as well.
Orr website is www.brivelmobile.example, please feel free to visit the site for some ideas. Thank you

Reason: I wanted to extend current deadline due to limited response so far. I can have the project due date extended til Nov 5th , I also need to make dessision by then. I'd like to get a few more ideas before picking the perfect design for our soft launch. Thank you

Industry/Entity Type

Telecommunications

Font styles to use
Serif

Requirements
Must have
• Logo
• brivelmobile.example
• Now I Can REALLY Hear You!
Should not have
• Address or phone number

```html
<!DOCTYPE html>
<html lang="en">
<head>
<meta charset="utf-8">
<title>Brivel Mobile – Phone Box Artwork</title>
<link rel="stylesheet" href="https://fonts.googleapis.com/css2?family=Rokkitt:wght@800&display=swap">
<style>
  :root {
    --backdrop: #8a8a8a;
    --box-black: #141414;
    --red-bright: #ee2f2a;
    --red-deep: #b8191a;
    --stripe-red: #a81a1c;
    --tree-red: rgba(120, 18, 18, .45);
    --ink-black: #0c0c0c;
    --ink-white: #ffffff;
    --phone-shell: #ececec;
    --phone-screen: #1b1b1b;
    --brand-red: #e3383a;
  }
  html, body {
    margin: 0;
    padding: 0;
    width: 907px;
    height: 1200px;
    overflow: hidden;
    background: var(--backdrop);
  }
  .canvas {
    position: relative;
    width: 907px;
    height: 1200px;
  }
  .panel {
    position: absolute;
    left: 155px;
    width: 597px;
    background: var(--box-black);
    overflow: hidden;
    box-shadow: 0 4px 14px rgba(0,0,0,.35);
  }
  .panel--front { top: 527px; height: 370px; }
  .panel--side  { top: 921px; height: 181px; }

  .red-band {
    position: absolute;
    top: 0;
    left: 82px;
    width: 282px;
    height: 100%;
    background: radial-gradient(ellipse at 60% 50%, var(--red-bright) 0%, #d82522 55%, var(--red-deep) 100%);
  }
  .tech-tree {
    position: absolute;
    left: 4px;
    top: 14px;
    width: 96px;
    height: 356px;
    background: linear-gradient(180deg, var(--tree-red), rgba(140, 22, 22, .6));
    border-radius: 48px 48px 0 0;
  }
  .slogan {
    position: absolute;
    right: 11px;
    top: 174px;
    margin: 0;
    font-family: "Rokkitt", Georgia, serif;
    font-weight: 800;
    text-align: right;
    line-height: 1;
  }
  .slogan span { display: block; }
  .slogan__lead  { font-size: 29px; color: var(--ink-black); }
  .slogan__focus { font-size: 50px; color: var(--ink-white); margin: 2px 0 0; }
  .slogan__close { font-size: 40px; color: var(--ink-black); margin-top: -2px; }

  .handset {
    position: absolute;
    left: 435px;
    top: 70px;
    width: 112px;
    height: 231px;
    border-radius: 16px;
    background: linear-gradient(180deg, var(--phone-shell), #cfcfcf);
  }
  .handset__screen {
    position: absolute;
    left: 6px;
    top: 16px;
    width: 100px;
    height: 199px;
    background: linear-gradient(180deg, #2a2a2a, var(--phone-screen) 60%, #050505);
  }
  .brand {
    position: absolute;
    left: 0;
    top: 82px;
    width: 100%;
    display: flex;
    flex-direction: column;
    align-items: center;
    gap: 6px;
  }
  .brand__dot {
    width: 22px;
    height: 22px;
    border-radius: 50%;
    background: var(--brand-red);
  }
  .brand__name {
    font-family: "Rokkitt", Georgia, serif;
    font-weight: 800;
    font-size: 10px;
    color: var(--brand-red);
    white-space: nowrap;
  }

  .stripe {
    position: absolute;
    top: 0;
    height: 100%;
    background: var(--stripe-red);
  }
  .stripe--one   { left: 38px;  width: 43px; }
  .stripe--two   { left: 106px; width: 22px; }
  .stripe--three { left: 168px; width: 16px; }
  .stripe--four  { left: 233px; width: 14px; }
</style>
</head>
<body>
<main class="canvas">
  <section class="panel panel--front">
    <div class="red-band">
      <div class="tech-tree" role="img" aria-label="Circuit tree illustration with round technology icons branching upward"></div>
      <h1 class="slogan">
        <span class="slogan__lead">Now I Can</span>
        <span class="slogan__focus">REALLY</span>
        <span class="slogan__close">Hear You!</span>
      </h1>
    </div>
    <div class="handset" role="img" aria-label="White smartphone showing the Brivel Mobile start screen">
      <div class="handset__screen">
        <div class="brand">
          <span class="brand__dot"></span>
          <span class="brand__name">brivelmobile.example</span>
        </div>
      </div>
    </div>
  </section>

  <section class="panel panel--side">
    <div class="red-band">
      <div class="stripe stripe--one"></div>
      <div class="stripe stripe--two"></div>
      <div class="stripe stripe--three"></div>
      <div class="stripe stripe--four"></div>
    </div>
  </section>
</main>
</body>
</html>
```